Brent's Lot Grading & Trenching

I would like to have business cards created for my land clearing company. We have excavators, skid steers, dump trucks, tractor trailer dump trailers, forestry mulchers along with all size tractors for pasture restoration and arena builds.

Target Market(s)

Both commercial and residential clients

Contact Information for Business Card

Name, phone number, email and website

Colors

Designer to choose colors to be used in the design.

```html
<!DOCTYPE html>
<html lang="en">
<head>
<meta charset="utf-8">
<title>Cedar Hollow Site Works — Business Card</title>
<link href="https://fonts.googleapis.com/css2?family=Outfit:wght@400;500;600;700&display=swap" rel="stylesheet">
<style>
  :root {
    --page: #ffffff;
    --card-navy: #19213f;
    --ink-light: #ffffff;
    --icon-teal: #3f6b84;
    --machine-yellow: #e2b22a;
    --machine-steel: #3a3d42;
  }
  html, body {
    margin: 0;
    padding: 0;
    width: 1200px;
    height: 1200px;
    overflow: hidden;
    background: var(--page);
    font-family: "Outfit", sans-serif;
  }
  .canvas {
    position: relative;
    width: 1200px;
    height: 1200px;
  }
  .business-card {
    position: absolute;
    left: 116px;
    top: 323px;
    width: 968px;
    height: 554px;
    border-radius: 38px;
    background: var(--card-navy);
    overflow: hidden;
    color: var(--ink-light);
  }
  .name-accent {
    position: absolute;
    left: 82px;
    top: 88px;
    width: 8px;
    height: 89px;
    background: var(--ink-light);
  }
  .person-name {
    position: absolute;
    left: 117px;
    top: 86px;
    margin: 0;
    font-size: 49px;
    font-weight: 600;
    line-height: 1;
    letter-spacing: 0.5px;
  }
  .person-title {
    position: absolute;
    left: 116px;
    top: 144px;
    margin: 0;
    font-size: 39px;
    font-weight: 400;
    line-height: 1;
    letter-spacing: 2.5px;
  }
  .machine-photo {
    position: absolute;
    left: 83px;
    top: 243px;
    width: 414px;
    height: 234px;
  }
  .contact-list {
    position: absolute;
    left: 575px;
    top: 117px;
    margin: 0;
    padding: 0;
    list-style: none;
  }
  .contact-item {
    position: relative;
    height: 62px;
    margin-bottom: 49px;
    padding-left: 73px;
    white-space: nowrap;
  }
  .contact-icon {
    position: absolute;
    left: 0;
    top: 0;
    width: 62px;
    height: 62px;
    border-radius: 50%;
    background: var(--ink-light);
    display: flex;
    align-items: center;
    justify-content: center;
  }
  .contact-label {
    display: block;
    padding-top: 3px;
    font-size: 24px;
    font-weight: 600;
    line-height: 1.1;
  }
  .contact-value {
    display: block;
    margin-top: 2px;
    font-size: 23px;
    font-weight: 400;
    line-height: 1.1;
    letter-spacing: 3.4px;
  }
</style>
</head>
<body>
<main class="canvas">
  <section class="business-card" aria-label="Cedar Hollow Site Works business card">
    <span class="name-accent"></span>
    <h1 class="person-name">JOHN DOE</h1>
    <p class="person-title">General Manager</p>

    <svg class="machine-photo" role="img" aria-label="Photo of a tracked skid steer with a forestry mulcher attachment" viewBox="0 0 414 234">
      <defs>
        <linearGradient id="machineTones" x1="0" y1="0" x2="1" y2="1">
          <stop offset="0" stop-color="var(--machine-yellow)"/>
          <stop offset="0.55" stop-color="#8a7634"/>
          <stop offset="1" stop-color="var(--machine-steel)"/>
        </linearGradient>
      </defs>
      <rect x="0" y="0" width="414" height="234" rx="14" fill="url(#machineTones)" opacity="0.85"/>
    </svg>

    <ul class="contact-list">
      <li class="contact-item">
        <span class="contact-icon">
          <svg width="46" height="46" viewBox="0 0 46 46" fill="none" stroke="var(--icon-teal)" stroke-width="2">
            <circle cx="23" cy="23" r="20"/>
            <ellipse cx="23" cy="23" rx="9" ry="20"/>
            <line x1="23" y1="3" x2="23" y2="43"/>
            <path d="M6 14 Q23 19 40 14"/>
            <path d="M3 23 H43"/>
            <path d="M6 32 Q23 27 40 32"/>
          </svg>
        </span>
        <span class="contact-label">Visit Our Website</span>
        <span class="contact-value">www.company.com</span>
      </li>
      <li class="contact-item">
        <span class="contact-icon">
          <svg width="38" height="28" viewBox="0 0 38 28" fill="none" stroke="var(--icon-teal)" stroke-width="2.4" stroke-linejoin="round">
            <rect x="2" y="2" width="34" height="24" rx="5"/>
            <path d="M4 5 L19 16 L34 5"/>
          </svg>
        </span>
        <span class="contact-label">Email Address</span>
        <span class="contact-value">john@company.com</span>
      </li>
      <li class="contact-item">
        <span class="contact-icon">
          <svg width="34" height="34" viewBox="0 0 24 24" fill="var(--icon-teal)">
            <path d="M6.6 10.8a15.1 15.1 0 0 0 6.6 6.6l2.2-2.2c.3-.3.7-.4 1-.2 1.1.4 2.3.6 3.6.6.6 0 1 .4 1 1V20c0 .6-.4 1-1 1A17 17 0 0 1 3 4c0-.6.4-1 1-1h3.5c.6 0 1 .4 1 1 0 1.3.2 2.5.6 3.6.1.3 0 .7-.2 1L6.6 10.8z"/>
          </svg>
        </span>
        <span class="contact-label">Office Number</span>
        <span class="contact-value">+009XXXXXXXX</span>
      </li>
    </ul>
  </section>
</main>
</body>
</html>
```